Banner-Design für Verkauf von Organic und fair Trade Mode
Zielgruppe
Wir starten einen Internetshop mit dem Verkauf von Organic und fair Trade Mode. Mit eigenen Designs aber wir verkaufen auch die Ware ohne Design.
Ein Shirt Designer ist angeschlossen so dass die Kunden auch die Shirts selbst gestalten können.
1. Textildruck Service
2. Verkauf von bedruckten und unbedruckten Shirts
3. Kunden können jedes Kleidungsstück im Shop individualisieren
Aufgabenstellung
Wir benötigen 4 Banner für unseren Shop. Die Bilder sollen über die komplette breite der Startseite des Shops gehen. Plan ist es die Banner in einem Slider nach einander laufen zu lassen.
1. Banner der auf unseren Printservice auch für Firmen, Schulen, Vereine etc. hinweist
2.Jedes Shirt kann selbst gestaltet werden
3. Hinweisbanner auf Fair Trade und Organic Kategorien im Shop
4. Banner für anstehende SALE und permanente Mengenrabatt Aktionen
5. Drucktechniken
Größe: 1240 * 400 px and smaller like 900 * ~ 400px.
Als Dateien sind das Firmenlogo sowie das Logo unsers Labels beigefügt außerdem ist ein Banner der jedoch nicht professionell genug ist angehängt.
Farbgebung des Shops: Header und navigation schwarz / grau,
Daher sind wir für alle Vorschläge offen und würden die Zusammenarbeit gerne weiter ausbauen da wir dringend Grafiker / Designer benötigen.

```html
<!DOCTYPE html>
<html lang="de">
<head>
<meta charset="utf-8">
<title>Shop-Banner – Printservice &amp; Organic</title>
<link rel="stylesheet" href="https://fonts.googleapis.com/css2?family=Open+Sans:wght@300;400;700&display=swap">
<style>
  :root {
    --page-bg: #ffffff;
    --panel-dark: #2e2e2e;
    --text-light: #ffffff;
    --brand-dark: #3a3a3a;
    --sky-pale: #eef3fb;
    --sky-mid: #cfdcef;
    --glass-blue: #2f6fc4;
    --glass-deep: #0f3c86;
    --forest-dark: #1a241c;
    --forest-mid: #2d3a2c;
    --plaid-red: #6a2026;
  }
  * { margin: 0; padding: 0; box-sizing: border-box; }
  html, body {
    width: 1200px;
    height: 675px;
    overflow: hidden;
    background: var(--page-bg);
    font-family: "Open Sans", sans-serif;
  }
  .canvas {
    position: relative;
    width: 1200px;
    height: 675px;
  }
  .banner {
    position: absolute;
    left: 212.5px;
    width: 775px;
    height: 250px;
    overflow: hidden;
  }
  .banner--printservice { top: 60.5px; }
  .banner--organic { top: 364.5px; }

  .banner__photo {
    position: absolute;
    inset: 0;
  }
  .banner--printservice .banner__photo {
    background:
      linear-gradient(90deg, var(--sky-pale) 0%, var(--sky-mid) 45%, #fff6e6 55%, var(--glass-blue) 72%, var(--glass-deep) 100%);
  }
  .banner--organic .banner__photo {
    background:
      linear-gradient(90deg, var(--forest-dark) 0%, var(--forest-mid) 45%, var(--plaid-red) 72%, var(--forest-dark) 100%);
  }

  .banner__headline-box {
    position: absolute;
    left: 30.5px;
    top: 30.5px;
    width: 356px;
    background: var(--panel-dark);
    color: var(--text-light);
    padding: 26px 20px 0 20.5px;
    text-transform: uppercase;
    font-size: 22.5px;
    line-height: 27.5px;
    letter-spacing: 0.1px;
  }
  .banner--printservice .banner__headline-box { height: 132px; }
  .banner--organic .banner__headline-box { height: 105px; }

  .headline__light { font-weight: 300; display: block; }
  .headline__bold { font-weight: 700; display: block; }

  .brand-name {
    position: absolute;
    left: 51px;
    font-weight: 700;
    font-size: 17px;
    letter-spacing: 1.5px;
    text-transform: uppercase;
  }
  .banner--printservice .brand-name { top: 192px; color: var(--brand-dark); }
  .banner--organic .brand-name { top: 192px; color: var(--text-light); }
</style>
</head>
<body>
<main class="canvas">

  <section class="banner banner--printservice">
    <div class="banner__photo" role="img" aria-label="Foto: Glasfassade eines Hochhauses vor hellem, sonnigem Himmel"></div>
    <h2 class="banner__headline-box">
      <span class="headline__light">Unser Printservice für</span>
      <span class="headline__bold">Unternehmen, Schulen,</span>
      <span class="headline__bold">Vereine und mehr.</span>
    </h2>
    <p class="brand-name">Nordfaden</p>
  </section>

  <section class="banner banner--organic">
    <div class="banner__photo" role="img" aria-label="Foto: Person im rot-schwarz karierten Hemd im Wald"></div>
    <h2 class="banner__headline-box">
      <span class="headline__light">Organic &amp; Fair Trade –</span>
      <span class="headline__bold">Hier im Shop.</span>
    </h2>
    <p class="brand-name">Nordfaden</p>
  </section>

</main>
</body>
</html>
```